Mobile dental anesthesiologist needs a postcard to market to other doctors

This postcard is intended to inform dentists in the California Central Coast region that I am available to travel to their office to serve their patient's anesthesia needs. It is important to know that other anesthesiologists are usually booked for weeks in advance and are very costly. Our market niche is greater availability and lower cost. I would prefer a 2 sided oversized postcard. The attached images are DIY projects I've done recently...You can see why I'm reaching out to professionals.

Dental

```html
<!DOCTYPE html>
<html lang="en">
<head>
<meta charset="utf-8">
<title>Harbor Ridge Dental Anesthesia – Postcard</title>
<link href="https://fonts.googleapis.com/css2?family=Open+Sans:wght@400;600;700&family=Roboto+Condensed:wght@400;700&family=Tinos&display=swap" rel="stylesheet">
<style>
  :root{
    --green:#4a8a3a;
    --lime:#9cc43a;
    --lime-text:#b9d94a;
    --blue:#2aa8e0;
    --orange:#ef6a1f;
    --ink:#444;
    --grey:#666;
    --paper:#fff;
    --bg:#ececec;
  }
  *{box-sizing:border-box;margin:0;padding:0}
  html,body{width:806px;height:1200px;overflow:hidden}
  body{background:var(--bg);font-family:"Open Sans",Arial,sans-serif;color:var(--ink);position:relative}
  .card{position:absolute;left:64px;width:680px;height:490px;background:var(--paper);overflow:hidden;box-shadow:0 3px 10px rgba(0,0,0,.25)}
  .card--front{top:86px}
  .card--back{top:622px}
  .card-art{position:absolute;inset:0;width:680px;height:490px}
  .abs{position:absolute}

  /* front */
  .brand-name{left:24px;top:58px;width:140px;font-size:15px;line-height:19px;font-weight:600;color:var(--green)}
  .brand-dot{left:70px;top:30px;width:22px;height:22px;border-radius:50%;background:var(--orange)}
  .brand-divider{left:158px;top:44px;width:1px;height:60px;background:#bbb}
  .headline{left:168px;top:44px;font-family:"Roboto Condensed",Arial,sans-serif;font-weight:700;font-size:29px;color:var(--blue);letter-spacing:.3px;line-height:32px}
  .tagline{left:169px;top:79px;font-family:"Roboto Condensed",Arial,sans-serif;font-size:15px;color:var(--grey);letter-spacing:.4px}
  .about-tab{left:0;top:137px;width:216px;height:26px;background:var(--orange);border-radius:0 13px 13px 0;color:#fff;font-family:"Roboto Condensed",Arial,sans-serif;font-weight:700;font-size:16px;line-height:26px;padding-left:26px;letter-spacing:.2px}
  .about-text{left:26px;top:176px;width:324px;font-family:"Tinos",Georgia,serif;font-size:12px;line-height:13.6px;text-align:justify;color:#333}
  .cta{left:24px;top:363px;color:#fff;font-weight:700}
  .cta__line{font-size:14px;line-height:20px}
  .cta__line--accent{font-size:16px;color:var(--lime-text);line-height:20px}
  .cta__line--big{font-size:18.5px;line-height:24px}
  .cta__phone{font-size:21px;font-weight:600;line-height:34px}
  .contact-divider{left:226px;top:368px;width:1px;height:74px;background:rgba(255,255,255,.35)}
  .contact{color:#fff;font-size:12px;font-weight:600;line-height:22px}
  .contact li{list-style:none;display:flex;align-items:center;gap:7px}
  .contact svg{width:11px;height:11px;flex:none}
  .contact--front{left:236px;top:394px}

  /* back */
  .name-pill{left:126px;top:60px;width:145px;height:56px;background:var(--orange);border-radius:0 28px 28px 0;padding:8px 0 0 20px;font-family:"Roboto Condensed",Arial,sans-serif;font-weight:700}
  .name-pill__name{color:#fff;font-size:15px;line-height:19px}
  .name-pill__phone{color:#3a2a20;font-size:15px;line-height:22px}
  .headshot-ring{left:30px;top:31px;width:112px;height:112px;border-radius:50%;background:var(--blue);padding:5px}
  .headshot{width:102px;height:102px;border-radius:50%;background:radial-gradient(circle at 50% 40%,#9a9a9a,#4a4a4a);border:3px solid #fff}
  .pitch{left:28px;top:158px;font-family:"Roboto Condensed",Arial,sans-serif}
  .pitch__strong{font-size:18px;font-weight:700;color:var(--green);line-height:22px}
  .pitch__soft{font-size:19.5px;color:var(--grey);line-height:24px}
  .benefits{left:28px;top:227px;font-size:11.5px;font-weight:700;color:#222;line-height:14.2px}
  .benefits li{list-style:none;padding-left:12px;position:relative}
  .benefits li::before{content:"";position:absolute;left:0;top:5px;width:5px;height:5px;border-radius:50%;background:var(--orange)}
  .region{left:28px;top:311px;font-family:"Roboto Condensed",Arial,sans-serif;font-weight:700}
  .region__from{font-size:16.5px;color:var(--grey);line-height:22px}
  .region__to{font-size:28px;color:var(--orange);line-height:34px}
  .contact--back{left:28px;top:436px;font-size:11.5px;line-height:16px}
  .stamp-box{left:575px;top:41px;width:56px;height:75px;border:1px solid #777}
</style>
</head>
<body>

<section class="card card--front" aria-label="Postcard front">
  <svg class="card-art" viewBox="0 0 680 490" aria-hidden="true">
    <defs>
      <linearGradient id="frontWash" x1="0" y1="0" x2="1" y2="0">
        <stop offset="0" stop-color="#fff"/><stop offset="1" stop-color="#f1f1f1"/>
      </linearGradient>
    </defs>
    <rect width="680" height="490" fill="url(#frontWash)"/>
    <circle cx="545" cy="232" r="184" fill="none" stroke="var(--lime)" stroke-width="7"/>
    <circle cx="545" cy="232" r="173" fill="none" stroke="var(--orange)" stroke-width="7"/>
    <path d="M0 318 C150 293 300 313 420 353 C440 360 458 366 472 372 C456 369 438 364 420 360 C300 322 150 302 0 327 Z" fill="var(--blue)"/>
    <path d="M0 333 C150 308 300 328 420 368 C520 402 610 408 680 383 L680 395 C610 420 520 414 420 380 C300 340 150 320 0 345 Z" fill="var(--lime)"/>
    <path d="M0 345 C150 320 300 340 420 380 C520 414 610 420 680 395 L680 490 L0 490 Z" fill="var(--green)"/>
  </svg>

  <div class="abs brand-dot"></div>
  <div class="abs brand-name">Harbor Ridge<br>Dental Anesthesia</div>
  <div class="abs brand-divider"></div>
  <div class="abs headline">DENTAL ANESTHESIA</div>
  <div class="abs tagline">OPENING DOORS TO TREATMENT</div>

  <div class="abs about-tab">ABOUT DR. MARCUS HALE</div>
  <p class="abs about-text">Some patients either require or would greatly benefit from treatment under anesthesia. You have seen them in your practice: the very young, those with special needs, the extremely anxious, and those undergoing invasive procedures. Put your patients and their families at ease by offering safe and effective anesthesia. Dr. Marcus Hale is a Dentist Anesthesiologist with experience in treating patients with a wide spectrum of ages and conditions.</p>

  <div class="abs" role="img" aria-label="Photo of a smiling dentist with a young boy in the dental chair" style="left:384px;top:72px;width:322px;height:322px;border-radius:50%;border:4px solid #fff;background:radial-gradient(circle at 55% 35%,#f3efe9,#d9d2c8 55%,#9fb2bf)"></div>

  <div class="abs cta">
    <div class="cta__line">Call to schedule a discussion</div>
    <div class="cta__line cta__line--accent">of how anesthesia may</div>
    <div class="cta__line cta__line--big">benefit your practice</div>
    <div class="cta__phone">555-014-2870</div>
  </div>
  <div class="abs contact-divider"></div>
  <ul class="abs contact contact--front">
    <li><svg viewBox="0 0 12 12"><rect x="0.5" y="2" width="11" height="8" fill="var(--lime)"/><path d="M0.5 2 L6 6.5 L11.5 2" fill="none" stroke="var(--green)" stroke-width="1"/></svg>mhale.dds@example.com</li>
    <li><svg viewBox="0 0 12 12"><circle cx="6" cy="6" r="5.3" fill="none" stroke="var(--lime)" stroke-width="1.3"/><path d="M0.8 6 H11.2 M6 0.8 C3 4 3 8 6 11.2 M6 0.8 C9 4 9 8 6 11.2" fill="none" stroke="var(--lime)" stroke-width="1"/></svg>www.marcushaledds.com</li>
  </ul>
</section>

<section class="card card--back" aria-label="Postcard back">
  <svg class="card-art" viewBox="0 0 680 490" aria-hidden="true">
    <defs>
      <linearGradient id="backWash" x1="0" y1="0" x2="1" y2="0">
        <stop offset="0" stop-color="#fff"/><stop offset="1" stop-color="#ececec"/>
      </linearGradient>
    </defs>
    <rect width="680" height="490" fill="url(#backWash)"/>
    <path d="M0 372 C120 345 250 362 360 395 L420 412 L420 420 L360 404 C250 372 120 358 0 386 Z" fill="var(--blue)"/>
    <path d="M0 384 C120 360 250 382 360 414 L420 430 L420 442 L360 426 C250 396 120 378 0 402 Z" fill="var(--lime)"/>
    <path d="M0 400 C120 378 250 398 360 430 L420 446 L420 490 L0 490 Z" fill="var(--green)"/>
    <path d="M438 0 C470 110 455 210 395 300 C355 370 340 430 338 490 H680 V0 Z" fill="#fff"/>
    <path d="M460 0 C490 120 470 220 410 310 C370 380 355 440 354 490 L346 490 C347 432 360 372 400 304 C458 214 478 118 448 0 Z" fill="var(--lime)"/>
    <path d="M478 40 C505 140 485 230 430 310 C395 365 382 420 380 490 L374 490 C375 420 388 360 424 304 C478 224 496 140 470 40 Z" fill="var(--blue)"/>
    <path d="M438 0 C470 110 455 210 395 300 C355 370 340 430 338 490 L326 490 C328 428 344 366 386 294 C444 204 460 108 428 0 Z" fill="var(--orange)"/>
    <circle cx="391" cy="268" r="60" fill="var(--orange)"/>
  </svg>

  <div class="abs" role="img" aria-label="Close-up photo of a doctor's hand holding a stethoscope with dental icons" style="left:337px;top:214px;width:108px;height:108px;border-radius:50%;border:3px solid #fff;background:radial-gradient(circle at 45% 40%,#f4f7fa,#b9cfe0 70%,#8aa6bd)"></div>

  <div class="abs name-pill">
    <div class="name-pill__name">DR. MARCUS HALE</div>
    <div class="name-pill__phone">555.014.2870</div>
  </div>
  <div class="abs headshot-ring">
    <div class="headshot" role="img" aria-label="Black and white portrait photo of the doctor in a suit"></div>
  </div>

  <div class="abs pitch">
    <div class="pitch__strong">Anesthesia can open doors to treatment</div>
    <div class="pitch__soft">that would otherwise never happen</div>
  </div>
  <ul class="abs benefits">
    <li>Your Patients</li>
    <li>Your Office</li>
    <li>Safe and Effective</li>
    <li>No Anesthesia Billing</li>
    <li>Headaches—leave that to us!</li>
  </ul>
  <div class="abs region">
    <div class="region__from">Serving the Central Coast from Camarillo</div>
    <div class="region__to">to San Luis Obispo</div>
  </div>
  <ul class="abs contact contact--back">
    <li><svg viewBox="0 0 12 12"><rect x="0.5" y="2" width="11" height="8" fill="var(--lime)"/><path d="M0.5 2 L6 6.5 L11.5 2" fill="none" stroke="var(--green)" stroke-width="1"/></svg>mhale.dds@example.com</li>
    <li><svg viewBox="0 0 12 12"><circle cx="6" cy="6" r="5.3" fill="none" stroke="var(--lime)" stroke-width="1.3"/><path d="M0.8 6 H11.2 M6 0.8 C3 4 3 8 6 11.2 M6 0.8 C9 4 9 8 6 11.2" fill="none" stroke="var(--lime)" stroke-width="1"/></svg>www.marcushaledds.com</li>
  </ul>

  <div class="abs stamp-box"></div>
</section>

</body>
</html>
```